Business card design for IT consulting company

Looking for a simple, modern, clean business card design.
Open to reworking our existing logo.

Attached is our current business cards which we do not like.
Ideally double sided with something simple on the back.
Rectangle / Horizonal only.
No rounded edges on the card.
White as the dominate color is preferred.

Target Market(s)

clients, legal, oil & gas, medical, professionals

Industry/Entity Type

IT, tech, consulting

Contact Information for Business Card

Name, Title, email, phone, cell, website

Font styles to use
Sans Serif

Requirements
Must have
• Clean design
Should not have
• loud colors or unusual fonts, etc

```html
<!DOCTYPE html>
<html lang="en">
<head>
<meta charset="utf-8">
<title>Northgrid – Business Card</title>
<link rel="stylesheet" href="https://fonts.googleapis.com/css2?family=Arimo:wght@400;700&display=swap">
<style>
  :root {
    --backdrop: #e2e3e2;
    --card: #f7f7f7;
    --ink: #3b3b3d;
    --ink-soft: #555558;
    --accent-blue: #4aa3d3;
    --brand-navy: #312f6b;
  }
  * { box-sizing: border-box; margin: 0; padding: 0; }
  html, body {
    width: 1200px; height: 1200px; overflow: hidden;
    background: var(--backdrop);
    font-family: "Arimo", Helvetica, Arial, sans-serif;
    color: var(--ink);
  }
  .sheet {
    width: 1200px; height: 1200px;
    display: flex; flex-direction: column; align-items: center; justify-content: center;
    gap: 80px;
  }
  .card {
    position: relative;
    width: 700px; height: 400px;
    background: var(--card);
    box-shadow: 0 2px 6px rgba(0,0,0,0.08), 0 12px 30px rgba(0,0,0,0.06);
  }
  .brand {
    display: flex; align-items: center; gap: 12px;
    color: var(--brand-navy);
    font-weight: 700;
  }
  .brand-mark { background: var(--brand-navy); display: block; }
  .card-front .brand {
    position: absolute; left: 0; width: 350px; top: 0; height: 400px;
    justify-content: center; font-size: 32px;
  }
  .card-front .brand-mark { width: 24px; height: 24px; }
  .divider {
    position: absolute; left: 350px; top: 60px;
    width: 3px; height: 280px; background: var(--accent-blue);
  }
  .details { position: absolute; left: 395px; top: 88px; }
  .person-name { font-size: 34px; font-weight: 700; letter-spacing: 0.5px; line-height: 1; }
  .person-title { font-size: 16px; color: var(--ink-soft); margin-top: 6px; }
  .contact-list { list-style: none; margin-top: 30px; }
  .contact-item {
    display: flex; align-items: center; gap: 14px;
    font-size: 19px; color: var(--ink); margin-bottom: 14px;
  }
  .contact-icon {
    width: 28px; height: 28px; border-radius: 5px;
    background: var(--accent-blue);
    display: flex; align-items: center; justify-content: center; flex: none;
  }
  .contact-icon svg { width: 18px; height: 18px; }
  .card-back { display: flex; align-items: center; justify-content: center; }
  .card-back .brand { font-size: 40px; gap: 14px; }
  .card-back .brand-mark { width: 30px; height: 30px; }
</style>
</head>
<body>
<main class="sheet">
  <section class="card card-front" aria-label="Card front">
    <div class="brand"><span class="brand-mark"></span>Northgrid</div>
    <div class="divider"></div>
    <div class="details">
      <h1 class="person-name">DANIEL PARK</h1>
      <p class="person-title">IT Consultant</p>
      <ul class="contact-list">
        <li class="contact-item">
          <span class="contact-icon"><svg viewBox="0 0 18 18" fill="none" stroke="#fff" stroke-width="1.5"><rect x="2" y="4" width="14" height="10"/><path d="M2 4l7 6 7-6M2 14l5-5M16 14l-5-5"/></svg></span>
          daniel.park@northgrid.ca
        </li>
        <li class="contact-item">
          <span class="contact-icon"><svg viewBox="0 0 18 18"><path fill="#fff" d="M5 2l3 3-1.6 1.8a9 9 0 0 0 4.8 4.8L13 10l3 3-2 2.5C8.5 15 3 9.5 2.5 4z"/></svg></span>
          (555) 014-2201
        </li>
        <li class="contact-item">
          <span class="contact-icon"><svg viewBox="0 0 18 18" fill="none" stroke="#fff" stroke-width="1.5"><rect x="5" y="2" width="8" height="14" rx="1.5"/><path d="M8 13.5h2"/></svg></span>
          (555) 016-7430
        </li>
        <li class="contact-item">
          <span class="contact-icon"><svg viewBox="0 0 18 18" fill="none" stroke="#fff" stroke-width="1.3"><circle cx="9" cy="9" r="6.5"/><ellipse cx="9" cy="9" rx="3" ry="6.5"/><path d="M2.5 9h13M4 5.5h10M4 12.5h10"/></svg></span>
          www.northgrid.ca
        </li>
      </ul>
    </div>
  </section>

  <section class="card card-back" aria-label="Card back">
    <div class="brand"><span class="brand-mark"></span>Northgrid</div>
  </section>
</main>
</body>
</html>
```